New business card for civil engineering company - "Keystone Audit"

We need a business card designed for our new structural engineering company.

The company name is "Keystone Audit" logo files attached.

We would like the following:
* Two-sided card
* Simple design

Information to be placed on the card:
Name - Marcus Dellow
Job Title - Director / Structural Engineer
Credentials - BEng(Hons), CPEng, CMengNZ, IntPE(NZ)
Email - marcus.dellow@keystoneaudit.co.nz
mobile - 0219364058
website - www.keystoneaudit.co.nz

```html
<!DOCTYPE html>
<html lang="en">
<head>
<meta charset="utf-8">
<title>Keystone Audit – Business Card</title>
<link rel="stylesheet" href="https://fonts.googleapis.com/css2?family=Lato:wght@400;700;900&display=swap">
<style>
  :root {
    --stage: #2b2b2d;
    --card-dark: #3c3c3f;
    --card-light: #ffffff;
    --ink: #2a2a2a;
    --ink-soft: #555a60;
    --brand-blue: #2f7fc1;
    --band-dark: #3a3a3c;
    --back-text: #e6e6e6;
    --back-muted: #a9a9ad;
  }
  * { box-sizing: border-box; margin: 0; padding: 0; }
  html, body {
    width: 1200px; height: 997px; overflow: hidden;
    background: var(--stage);
    font-family: "Lato", sans-serif;
  }
  .card {
    position: absolute;
    width: 600px; height: 340px;
    border-radius: 26px;
    overflow: hidden;
    box-shadow: 0 18px 40px rgba(0,0,0,.45);
  }
  /* Back side */
  .card--back {
    left: 300px; top: 100px;
    background: var(--card-dark);
    display: flex; flex-direction: column; align-items: center; justify-content: center;
    text-align: center;
  }
  .card--back .brand-name {
    color: var(--back-text);
    font-size: 46px; font-weight: 700; letter-spacing: 3px;
  }
  .card--back .brand-tagline {
    color: var(--back-muted);
    font-size: 13px; letter-spacing: 4px; margin-top: 6px;
  }
  .card--back .brand-web {
    color: var(--back-text);
    font-size: 17px; font-weight: 700; letter-spacing: 2px; margin-top: 26px;
  }
  /* Front side */
  .card--front {
    left: 300px; top: 520px;
    background: var(--card-light);
  }
  .front-logo {
    position: absolute; right: 34px; top: 40px; text-align: right;
  }
  .front-logo .brand-name {
    color: var(--ink); font-size: 24px; font-weight: 700; letter-spacing: 2px;
  }
  .front-logo .brand-tagline {
    color: var(--ink-soft); font-size: 8px; letter-spacing: 2.4px; margin-top: 2px;
  }
  .rule {
    position: absolute; left: 196px; right: 34px; top: 132px;
    height: 1.5px; background: var(--brand-blue);
  }
  .person { position: absolute; left: 30px; top: 116px; }
  .person .name { font-size: 22px; font-weight: 700; color: var(--brand-blue); }
  .person .name span { font-weight: 400; }
  .person .credentials { font-size: 12.5px; color: var(--ink); margin-top: 2px; }
  .person .role { font-size: 13.5px; color: var(--brand-blue); margin-top: 1px; }
  .contacts { position: absolute; left: 30px; top: 218px; list-style: none; }
  .contacts li {
    display: flex; align-items: center; gap: 12px;
    font-size: 14px; color: var(--ink); margin-bottom: 9px;
  }
  .contacts svg { width: 18px; height: 18px; flex: none; }
  .company { position: absolute; right: 34px; top: 148px; text-align: right; }
  .company .company-name { font-size: 13px; font-weight: 700; color: var(--brand-blue); letter-spacing: .5px; }
  .company .address { font-size: 12.5px; color: var(--ink); margin-top: 12px; }
  .footer-band { position: absolute; left: 0; bottom: 0; width: 600px; height: 80px; }
  .footer-web {
    position: absolute; right: 34px; bottom: 22px;
    color: #ffffff; font-size: 17px; font-weight: 700; letter-spacing: 2px;
  }
</style>
</head>
<body>

<section class="card card--back" aria-label="Card back">
  <div class="brand-name">KEYSTONE AUDIT</div>
  <div class="brand-tagline">PEER REVIEW SPECIALISTS</div>
  <div class="brand-web">www.keystoneaudit.co.nz</div>
</section>

<section class="card card--front" aria-label="Card front">
  <div class="front-logo">
    <div class="brand-name">KEYSTONE AUDIT</div>
    <div class="brand-tagline">PEER REVIEW SPECIALISTS</div>
  </div>

  <div class="rule"></div>

  <div class="person">
    <div class="name">Marcus <span>Dellow</span></div>
    <div class="credentials">BEng(Hons), CPEng, CMengNZ, IntPE(NZ)</div>
    <div class="role">Director/ Structural Engineer</div>
  </div>

  <div class="company">
    <div class="company-name">KEYSTONE AUDIT</div>
    <div class="address">#118, harbour lane street, Canada.</div>
  </div>

  <ul class="contacts">
    <li>
      <svg viewBox="0 0 18 18" aria-hidden="true"><circle cx="9" cy="9" r="9" fill="var(--brand-blue)"/><path d="M5.5 7.2c0-1 .8-1.7 3.5-1.7s3.5.7 3.5 1.7l-1.3.3-.4-1.1H7.2l-.4 1.1zM6.2 8.4h5.6l.6 3.6H5.6z" fill="#fff"/></svg>
      0219364058
    </li>
    <li>
      <svg viewBox="0 0 18 18" aria-hidden="true"><circle cx="9" cy="9" r="9" fill="var(--brand-blue)"/><rect x="5" y="6" width="8" height="6" fill="none" stroke="#fff" stroke-width="1.1"/><path d="M5 6l4 3.2L13 6" fill="none" stroke="#fff" stroke-width="1.1"/></svg>
      marcus.dellow@keystoneaudit.co.nz
    </li>
  </ul>

  <svg class="footer-band" viewBox="0 0 600 80" aria-hidden="true">
    <path d="M0 66 H288 L290 72 H0 Z" fill="var(--brand-blue)"/>
    <path d="M0 70 H300 L302 80 H0 Z" fill="var(--brand-blue)"/>
    <path d="M258 80 C280 80 282 28 312 28 H600 V80 Z" fill="var(--band-dark)"/>
  </svg>
  <div class="footer-web">www.keystoneaudit.co.nz</div>
</section>

</body>
</html>
```